CalmPath Nurses' Manifesto

Design a manifesto to inspire and motivate nurses to work at minimum standards of excellence in their nursing practice.

The manifesto will become a feature of our website, at conferences, workshops and retreats. It will also be featured on other marketing tools.

Primary Market:
Nurses and/or other healthcare professionals (specifically Doctors, Occupational Therapists, Psychologists and Social Workers).

However the manifesto is equally applicable to all nurses and healthcare professionals from new graduates to very experienced senior clinicians, administration officers,managers and healthcare executive personnel.

Mainly females and primarily 35 to 65 years old, which suggests people in this target age group have extensive experience, but have become jaded'.

The purpose of our business is to assist healthcare professionals, primarily nurses, to maintain their enthusiasm and excellence in service provision, for their benefit as well as the benefit of the clients.

I have attached:
File 1: Copy Samples and examples: which has the copy for the manifesto, examples that appeal to us and our 3 attempts.
File 2: Our colour Spec Sheet, HOWEVER the colours are not necessary limited to these colours. These colours are not in the logo that will be on the manifesto. The colours on the logo attached can/or also be used.
File 3: Prototype logo. The final logo will be available within 3 to 4 days.

Requirements
Must have
• Must use the copy as per the attached file.

It should be contemporary, eye catching and motivational.

Sample 1 on the attached file (File 3: copy, samples and examples_554207 saturday, 29 june 2013 06:24:3030) Is close to what we are looking for.
Should not have
• MUST BE EASY TO READ. Each line MUST be clearly defined from each other.

```html
<!DOCTYPE html>
<html lang="en">
<head>
<meta charset="utf-8">
<title>CalmPath Nurses' Manifesto</title>
<link rel="stylesheet" href="https://fonts.googleapis.com/css2?family=Archivo+Black&family=Arimo:wght@700&family=Kaushan+Script&family=Oswald:wght@400;500&family=Yellowtail&family=Questrial&display=swap">
<style>
  :root {
    --paper: #efefef;
    --green: #22a84a;
    --lime: #8cc63f;
    --teal: #17a7a0;
    --deep-teal: #1e5f5b;
    --ink: #1e4a4c;
    --lens: #e4e6e6;
  }
  html, body {
    margin: 0;
    padding: 0;
    width: 849px;
    height: 1200px;
    overflow: hidden;
    background: var(--paper);
  }
  .manifesto { display: block; width: 849px; height: 1200px; }
  .bold-sans { font-family: "Arimo", Arial, sans-serif; font-weight: 700; }
  .heavy-sans { font-family: "Archivo Black", "Arial Black", sans-serif; }
  .condensed { font-family: "Oswald", "Arial Narrow", sans-serif; font-weight: 500; }
  .brush { font-family: "Kaushan Script", cursive; }
  .flowing { font-family: "Yellowtail", cursive; }
  .brand-name { font-family: "Questrial", Arial, sans-serif; }
  .c-green { fill: var(--green); }
  .c-lime { fill: var(--lime); }
  .c-teal { fill: var(--teal); }
  .c-deep { fill: var(--deep-teal); }
  .c-ink { fill: var(--ink); }
  .c-white { fill: #ffffff; }
  .rule-green { stroke: var(--green); fill: none; }
  .rule-teal { stroke: var(--teal); fill: none; }
  .rule-deep { stroke: var(--deep-teal); fill: none; }
  .connector { stroke: var(--teal); stroke-width: 2.5; stroke-dasharray: 6 5; fill: none; }
</style>
</head>
<body>
<svg class="manifesto" viewBox="0 0 768 1086" preserveAspectRatio="none" xmlns="http://www.w3.org/2000/svg">
  <defs>
    <radialGradient id="lens-fill" cx="45%" cy="40%" r="60%">
      <stop offset="0" stop-color="#f4f5f5"/>
      <stop offset="1" stop-color="#dcdfdf"/>
    </radialGradient>
  </defs>

  <rect class="background" width="768" height="1086" fill="var(--paper)"/>

  <!-- frame lines -->
  <g class="frame">
    <line class="rule-green" x1="20" y1="0" x2="20" y2="1062" stroke-width="5"/>
    <line class="rule-green" x1="20" y1="42" x2="72" y2="42" stroke-width="5"/>
    <line class="rule-teal" x1="757" y1="18" x2="757" y2="500" stroke-width="2"/>
    <line class="rule-teal" x1="395" y1="18" x2="757" y2="18" stroke-width="2"/>
    <line class="rule-green" x1="20" y1="172" x2="365" y2="172" stroke-width="3"/>
    <line class="rule-teal" x1="372" y1="172" x2="757" y2="172" stroke-width="2"/>
    <line class="rule-deep" x1="330" y1="565" x2="330" y2="598" stroke-width="2"/>
    <line class="rule-teal" x1="352" y1="594" x2="757" y2="594" stroke-width="2"/>
    <line class="rule-deep" x1="35" y1="720" x2="325" y2="720" stroke-width="2.5"/>
    <line class="rule-deep" x1="35" y1="720" x2="35" y2="808" stroke-width="2.5"/>
    <line class="rule-deep" x1="38" y1="895" x2="115" y2="895" stroke-width="2.5"/>
    <line class="rule-deep" x1="38" y1="895" x2="38" y2="975" stroke-width="2.5"/>
    <line class="rule-deep" x1="38" y1="975" x2="188" y2="975" stroke-width="2.5"/>
    <line class="rule-teal" x1="690" y1="968" x2="742" y2="968" stroke-width="2"/>
  </g>

  <!-- health -->
  <text class="bold-sans c-green" x="36" y="30" font-size="22" textLength="670" lengthAdjust="spacingAndGlyphs">ook after yourself and value your health as much as you</text>
  <text class="bold-sans c-green" x="73" y="48" font-size="18" textLength="318" lengthAdjust="spacingAndGlyphs">value the health of others.</text>

  <text class="brush c-deep" x="30" y="90" font-size="40" textLength="365" lengthAdjust="spacingAndGlyphs">Deliver care skillfully,</text>
  <text class="condensed c-teal" x="398" y="77" font-size="40" textLength="360" lengthAdjust="spacingAndGlyphs">Delight your clients and colleagues</text>
  <text class="condensed c-teal" x="398" y="128" font-size="40" textLength="330" lengthAdjust="spacingAndGlyphs">by exceeding their expectations.</text>
  <text class="bold-sans c-lime" x="35" y="130" font-size="20" textLength="352" lengthAdjust="spacingAndGlyphs">Respect the limits of people’s</text>
  <text class="bold-sans c-lime" x="33" y="162" font-size="20" textLength="608" lengthAdjust="spacingAndGlyphs">knowledge  and share your knowledge generously.</text>

  <text class="condensed c-green" x="372" y="198" font-size="28" textLength="380" lengthAdjust="spacingAndGlyphs">Learn something new each day.</text>
  <text class="heavy-sans c-deep" x="434" y="258" font-size="62">B</text>
  <text class="condensed c-deep" x="472" y="258" font-size="44" textLength="283" lengthAdjust="spacingAndGlyphs">e a lifelong learner</text>

  <text class="heavy-sans c-green" x="33" y="285" font-size="44">S</text>
  <text class="bold-sans c-teal" x="70" y="285" font-size="20">up</text>
  <text class="bold-sans c-green" x="410" y="288" font-size="22" textLength="345" lengthAdjust="spacingAndGlyphs">...port your colleagues and</text>
  <text class="bold-sans c-green" x="415" y="322" font-size="22" textLength="335" lengthAdjust="spacingAndGlyphs">champion  their  purpose</text>

  <!-- lens -->
  <g class="lens-heading">
    <circle cx="262" cy="318" r="145" fill="url(#lens-fill)" stroke="#ffffff" stroke-width="3"/>
    <text class="heavy-sans c-teal" x="100" y="252" font-size="56" textLength="322" lengthAdjust="spacingAndGlyphs">Nurse with open</text>
    <text class="heavy-sans c-teal" x="118" y="336" font-size="62" textLength="290" lengthAdjust="spacingAndGlyphs">hands, hearts</text>
    <text class="heavy-sans c-teal" x="160" y="402" font-size="44" textLength="202" lengthAdjust="spacingAndGlyphs">and minds</text>
  </g>

  <text class="bold-sans c-deep" x="405" y="360" font-size="20" textLength="280" lengthAdjust="spacingAndGlyphs">Smile and infect others</text>
  <text class="bold-sans c-deep" x="398" y="390" font-size="20" textLength="270" lengthAdjust="spacingAndGlyphs">with your happiness</text>
  <text class="bold-sans c-deep" x="372" y="420" font-size="20" textLength="150" lengthAdjust="spacingAndGlyphs">and have fun</text>
  <text class="bold-sans c-green" x="530" y="420" font-size="20">!</text>

  <g class="smile-icon" fill="var(--green)">
    <circle cx="688" cy="380" r="3.5"/>
    <circle cx="680" cy="392" r="3.5"/>
    <path d="M666 404 Q690 420 702 384" stroke="var(--green)" stroke-width="4" fill="none"/>
  </g>

  <!-- trust -->
  <text class="flowing c-lime" x="18" y="520" font-size="210">T</text>
  <text class="flowing c-lime" x="122" y="470" font-size="34" textLength="640" lengthAdjust="spacingAndGlyphs">rust Your knowledge and seek advice only from respected Sources.</text>

  <!-- diversity -->
  <rect class="diversity-band" x="295" y="508" width="473" height="52" fill="var(--teal)"/>
  <text class="condensed c-white" x="302" y="555" font-size="40" textLength="458" lengthAdjust="spacingAndGlyphs">Celebrate, Respect and Value the</text>
  <text class="bold-sans c-teal" x="355" y="587" font-size="20" textLength="365" lengthAdjust="spacingAndGlyphs">diversity of Australian culture.</text>

  <text class="bold-sans c-ink" x="35" y="587" font-size="24" textLength="290" lengthAdjust="spacingAndGlyphs">Always do the right thing</text>
  <text class="bold-sans c-ink" x="78" y="628" font-size="24" textLength="210" lengthAdjust="spacingAndGlyphs">without exception.</text>
  <text class="bold-sans c-green" x="352" y="632" font-size="24" textLength="390" lengthAdjust="spacingAndGlyphs">Seek success firstly from within.</text>

  <text class="condensed c-teal" x="35" y="683" font-size="26" font-weight="400" textLength="270" lengthAdjust="spacingAndGlyphs">Respond to complex situations</text>
  <text class="flowing c-deep" x="338" y="702" font-size="56" textLength="422" lengthAdjust="spacingAndGlyphs">Always be solution focused.</text>

  <path class="connector" d="M306 676 H325 V862 M325 870 V878 H150 V886 H185"/>

  <text class="bold-sans c-teal" x="38" y="745" font-size="20" textLength="520" lengthAdjust="spacingAndGlyphs">•You are unique, revel in your individuality.</text>
  <text class="bold-sans c-teal" x="38" y="775" font-size="20" textLength="400" lengthAdjust="spacingAndGlyphs">•Only follow exceptional leaders.</text>
  <text class="bold-sans c-teal" x="38" y="805" font-size="20" textLength="502" lengthAdjust="spacingAndGlyphs">•If there is no one left to follow, then lead</text>
  <text class="bold-sans c-green" x="544" y="805" font-size="40">!</text>

  <text class="bold-sans c-teal" x="578" y="748" font-size="15" font-weight="400" textLength="182" lengthAdjust="spacingAndGlyphs">Adopt a ‘can do’ attitude</text>
  <text class="bold-sans c-teal" x="612" y="772" font-size="15" textLength="112" lengthAdjust="spacingAndGlyphs">to everything</text>
  <text class="bold-sans c-teal" x="592" y="798" font-size="15" textLength="145" lengthAdjust="spacingAndGlyphs">that comes your way.</text>

  <text class="brush c-green" x="35" y="862" font-size="40" textLength="725" lengthAdjust="spacingAndGlyphs">Always lead with purpose, passion and commitment.</text>
  <text class="condensed c-teal" x="195" y="890" font-size="18" font-weight="400" textLength="540" lengthAdjust="spacingAndGlyphs">innovatively, creatively and safely within the scope of your practice.</text>

  <text class="bold-sans c-ink" x="44" y="922" font-size="26" textLength="368" lengthAdjust="spacingAndGlyphs">Choose your thoughts wisely,</text>
  <text class="bold-sans c-ink" x="44" y="960" font-size="26" textLength="405" lengthAdjust="spacingAndGlyphs">they  create  your  reality.</text>

  <text class="flowing c-lime" x="496" y="958" font-size="60" textLength="248" lengthAdjust="spacingAndGlyphs">Live your dream</text>

  <!-- brand -->
  <g class="brand">
    <rect x="40" y="1020" width="50" height="50" fill="var(--lime)"/>
    <text class="brand-name c-ink" x="120" y="1058" font-size="34">CalmPath Solutions</text>
  </g>
</svg>
</body>
</html>
```